Folder & Business Card for Automation Company
Brightwell Torque Mfr.
Folder & Business Card for Automation Company - Manufacturing
Creative Brief
Professional
Darren Okafor
Vice President
4817 Halvern Road Merriam, KS 66209
do@brightwelltorquemfr.example
www.brightwelltorquemfr.example
Along with a business card we are looking for a design for the front cover of a folder to be used for sales literature. The cover should also include our logo.

```html
<!DOCTYPE html>
<html lang="en">
<head>
<meta charset="utf-8">
<title>Brightwell Torque Mfr. — Business Card</title>
<link href="https://fonts.googleapis.com/css2?family=Cinzel:wght@400;700&display=swap" rel="stylesheet">
<style>
  :root {
    --page-bg: #ecebe8;
    --card-white: #ffffff;
    --brand-red: #d71920;
    --brand-red-dark: #9e0f14;
    --charcoal: #2b2b2b;
    --charcoal-light: #4a4a4a;
    --ink: #2a2a2a;
    --text-light: #e8e8e8;
    --divider: #8a8a8a;
  }
  * { margin: 0; padding: 0; box-sizing: border-box; }
  html, body {
    width: 1200px; height: 873px; overflow: hidden;
    background: var(--page-bg);
  }
  .card {
    position: absolute; left: 100px; top: 166px;
    width: 1000px; height: 540px;
    border-radius: 34px; overflow: hidden;
    background: var(--card-white);
    box-shadow: 0 6px 18px rgba(0,0,0,0.18);
    font-family: "Cinzel", serif;
  }
  .card-backdrop { position: absolute; inset: 0; width: 100%; height: 100%; }
  .brand {
    position: absolute; left: 0; right: 0; top: 78px;
    display: flex; justify-content: center; align-items: center; gap: 22px;
  }
  .brand-dot {
    width: 40px; height: 40px; border-radius: 50%;
    background: var(--brand-red);
  }
  .brand-name {
    font-family: "Cinzel", serif; font-weight: 700;
    font-size: 56px; line-height: 1.02; letter-spacing: 2px;
    color: var(--ink);
  }
  .contact-block {
    position: absolute; top: 342px; left: 0; right: 0; height: 150px;
    color: var(--text-light);
  }
  .person {
    position: absolute; right: 520px; top: 14px; text-align: right;
  }
  .person-name { font-size: 26px; letter-spacing: 1px; }
  .person-title { font-size: 19px; margin-top: 2px; }
  .address {
    position: absolute; right: 520px; top: 90px; text-align: right;
    font-size: 19px; line-height: 1.35;
  }
  .divider {
    position: absolute; left: 500px; top: 10px; width: 1px; height: 135px;
    background: var(--divider);
  }
  .channels {
    position: absolute; left: 522px; top: 12px; list-style: none;
    font-size: 18px; letter-spacing: 0.5px;
  }
  .channels li {
    display: flex; align-items: center; gap: 12px; height: 34px;
  }
  .channels svg { width: 22px; height: 22px; flex: none; }
</style>
</head>
<body>
  <div class="card">
    <svg class="card-backdrop" viewBox="0 0 1000 540" preserveAspectRatio="none" aria-hidden="true">
      <defs>
        <radialGradient id="panelShade" cx="0.45" cy="0.55" r="0.8">
          <stop offset="0" stop-color="#4d4d4d"/>
          <stop offset="1" stop-color="#1f1f1f"/>
        </radialGradient>
        <linearGradient id="swoosh" x1="0" y1="0" x2="1" y2="0">
          <stop offset="0" stop-color="#b5121a"/>
          <stop offset="0.5" stop-color="#e0242b"/>
          <stop offset="1" stop-color="#b5121a"/>
        </linearGradient>
      </defs>
      <path d="M0 262 C180 300 420 318 620 292 C780 272 900 232 1000 214 L1000 540 L0 540 Z" fill="url(#swoosh)"/>
      <path d="M0 296 C200 330 430 338 640 310 C800 288 910 250 1000 236 L1000 540 L0 540 Z" fill="url(#panelShade)"/>
    </svg>

    <div class="brand">
      <span class="brand-dot"></span>
      <span class="brand-name">BRIGHTWELL<br>TORQUE</span>
    </div>

    <div class="contact-block">
      <div class="person">
        <div class="person-name">Darren Okafor</div>
        <div class="person-title">Vice President</div>
      </div>
      <div class="address">4817 Halvern Road Merriam,<br>KS 66209</div>
      <div class="divider"></div>
      <ul class="channels">
        <li>
          <svg viewBox="0 0 24 24"><circle cx="12" cy="12" r="11" fill="#e8e8e8"/><path d="M8.5 6.5l2 2-1.2 1.6c.8 1.8 2 3 3.8 3.8l1.6-1.2 2 2-1.4 1.8c-4.2-.6-7.8-4.2-8.4-8.4z" fill="#2b2b2b"/></svg>
          913-555-0148
        </li>
        <li>
          <svg viewBox="0 0 24 24"><circle cx="12" cy="12" r="11" fill="#e8e8e8"/><rect x="7" y="10" width="10" height="7" fill="#2b2b2b"/><rect x="9" y="6" width="6" height="4" fill="#2b2b2b"/></svg>
          913-555-0172
        </li>
        <li>
          <svg viewBox="0 0 24 24"><circle cx="12" cy="12" r="11" fill="#e8e8e8"/><rect x="6" y="8" width="12" height="8" fill="#2b2b2b"/><path d="M6 8l6 5 6-5" fill="none" stroke="#e8e8e8" stroke-width="1.2"/></svg>
          do@brightwelltorquemfr.example
        </li>
        <li>
          <svg viewBox="0 0 24 24"><circle cx="12" cy="12" r="11" fill="#e8e8e8"/><circle cx="12" cy="12" r="6.5" fill="none" stroke="#2b2b2b" stroke-width="1.4"/><path d="M5.5 12h13M12 5.5c-3 3.5-3 9.5 0 13M12 5.5c3 3.5 3 9.5 0 13" fill="none" stroke="#2b2b2b" stroke-width="1.2"/></svg>
          www.brightwelltorquemfr.example
        </li>
      </ul>
    </div>
  </div>
</body>
</html>
```